Freelance film producer/editor wants you to gleam nova!

'Gleam Nova' is my production business based in Melbourne, though I do a fair bit of work overseas. I'm a one woman show most of the time but enlist other crew members for larger projects. I manage productions from start to finish including producing, filming, editing, distribution, photography and animation.

My current tag line and details are as follows:

Petra Vandoren
Producer. Editor. Thinker.
[M] +61 492 157 630
[E] pv[at]brightpanel.com.au
www.brightpanel.com.au

I have a fairly wicked sense of humour and love a good pun, so feel free to work this into your design!

The final designs should demonstrate the areas I work in but not limited to. I'd rather not use old and typical "film" looking elements such as a clapper or negative reel. Having said that, the logo itself (attached) is quite typical because the first 'o' is a closed aperture and the second is a wide aperture. Happy for the logo to be pulled apart for the business card to be more interesting.

The majority of projects I work on are quite different and in some cases a bit crazy. Lots of travel involved. The main difference between me and other producers is that I don't say I work in 'film', even though i do. I want the card to leave me open to new roles and projects as opposed to squashing myself into one particular category.

I'm open to colour but prefer a simple design that isn't too hectic.

I have also attached an example I did like that was printed on plastic but then I realised so many other people had ripped it off....

I'm open to paper board or plastic (transparent) designs etc. One sided or two sided.

Thanks for sharing your ideas with me and please, go as nuts as you want to with this! :)

Target Market(s)

My clients range from non profits in health and educational institutions to record labels and well known artists. The business attracts corporates as well though the majority of my business is achieved through referral and word of mouth so most people will soon realise that my personality and work are very much intertwined and the reason they hire me for a job.

Industry/Entity Type

Business

Font styles to use
Other font styles liked:
• Eurostile or similar

Requirements
Must have
• I have a very open mind when it comes to design. I do like the existing tag line but if you can come up with something better I'm all ears! (and eyes)

Nice to have
• Back of the business card can be graphics, there can be transparent elements or holes, embossing options...
Should not have
• Besides my name, nothing should scream "I am woman!" because in my industry that's not a selling point.

The colour pink is a definite no.

```html
<!DOCTYPE html>
<html lang="en">
<head>
<meta charset="utf-8">
<title>Gleam Nova – Business Card</title>
<link rel="stylesheet" href="https://fonts.googleapis.com/css2?family=Quicksand:wght@300;400&family=Jura:wght@400;500&display=swap">
<style>
  :root {
    --page: #ffffff;
    --ink-cyan: #2fb3cf;
    --ink-cyan-soft: #5cbfd6;
    --ink-blue: #38b6e8;
    --dark-top: #1d2a30;
    --dark-mid: #2c3d45;
    --steel: #4a5c64;
    --sea-deep: #0b5d7c;
    --sea-bright: #0a9fd2;
    --band-teal: rgba(10, 70, 88, 0.75);
    --band-navy: rgba(6, 36, 62, 0.85);
    --band-accent: #2a7fa8;
    --grey-glow: #9aa3a6;
  }
  * { margin: 0; padding: 0; box-sizing: border-box; }
  html, body {
    width: 1200px;
    height: 1000px;
    overflow: hidden;
    background: var(--page);
  }
  .canvas {
    position: relative;
    width: 1200px;
    height: 1000px;
  }
  .card {
    position: absolute;
    border-radius: 14px;
    overflow: hidden;
  }

  /* Front */
  .card-front {
    left: 30px; top: 40px;
    width: 762px; height: 452px;
  }
  .front-upper {
    position: absolute; left: 0; top: 0;
    width: 100%; height: 225px;
    background: linear-gradient(100deg, var(--dark-top) 0%, var(--dark-mid) 45%, var(--steel) 80%, #6f7d83 100%);
  }
  .front-lower {
    position: absolute; left: 0; top: 225px;
    width: 100%; height: 227px;
    background: linear-gradient(160deg, var(--sea-deep) 0%, #0d7aa3 45%, var(--sea-bright) 85%, #2bb0dd 100%);
  }
  .brand-name {
    position: absolute;
    left: 56px; top: 116px;
    font-family: "Quicksand", sans-serif;
    font-weight: 300;
    font-size: 116px;
    line-height: 1;
    letter-spacing: 0;
    color: var(--ink-cyan);
    white-space: nowrap;
  }
  .tagline {
    position: absolute;
    left: 60px; top: 240px;
    font-family: "Quicksand", sans-serif;
    font-weight: 300;
    font-size: 30px;
    line-height: 1;
    color: var(--ink-cyan-soft);
    white-space: nowrap;
  }

  /* Back */
  .card-back {
    left: 411px; top: 517px;
    width: 762px; height: 450px;
    background:
      radial-gradient(ellipse at 95% 90%, var(--grey-glow) 0%, rgba(154,163,166,0) 45%),
      linear-gradient(110deg, #121b1f 0%, var(--dark-top) 25%, var(--dark-mid) 60%, var(--steel) 100%);
  }
  .icon-column {
    position: absolute; left: 70px; top: 0;
    width: 68px; height: 100%;
    background: var(--band-teal);
  }
  .web-band {
    position: absolute; left: 0; top: 360px;
    width: 100%; height: 66px;
    background: var(--band-navy);
  }
  .web-band-accent {
    position: absolute; left: 70px; top: 360px;
    width: 68px; height: 66px;
    background: var(--band-accent);
  }
  .contact-row {
    position: absolute;
    left: 0;
    width: 100%;
    height: 50px;
    display: flex;
    align-items: center;
  }
  .contact-icon {
    width: 68px;
    margin-left: 70px;
    display: flex;
    justify-content: center;
  }
  .contact-text {
    margin-left: 36px;
    font-family: "Jura", sans-serif;
    font-weight: 500;
    color: var(--ink-blue);
    white-space: nowrap;
    letter-spacing: 1px;
  }
  .row-name   { top: 35px;  } .row-name .contact-text   { font-size: 37px; }
  .row-role   { top: 107px; } .row-role .contact-text   { font-size: 39px; }
  .row-phone  { top: 183px; } .row-phone .contact-text  { font-size: 37px; }
  .row-email  { top: 258px; } .row-email .contact-text  { font-size: 31px; }
  .row-web    { top: 368px; } .row-web .contact-text    { font-size: 40px; margin-left: 40px; }
</style>
</head>
<body>
<main class="canvas">

  <section class="card card-front" aria-label="Business card front">
    <div class="front-upper" role="img" aria-label="Dark slate background with faint geometric triangle texture"></div>
    <div class="front-lower" role="img" aria-label="Blue geometric triangle texture with floating bubble rings"></div>
    <div class="brand-name">gleam nova</div>
    <div class="tagline">producer. editor. thinker.</div>
  </section>

  <section class="card card-back" aria-label="Business card back">
    <div class="icon-column"></div>
    <div class="web-band"></div>
    <div class="web-band-accent"></div>

    <div class="contact-row row-name">
      <span class="contact-icon">
        <svg width="30" height="32" viewBox="0 0 30 32" aria-hidden="true">
          <circle cx="15" cy="9" r="8" fill="#38b6e8"/>
          <path d="M1 32 V27 Q1 19 9 19 H21 Q29 19 29 27 V32 Z" fill="#38b6e8"/>
        </svg>
      </span>
      <span class="contact-text">Petra Vandoren</span>
    </div>

    <div class="contact-row row-role">
      <span class="contact-icon"></span>
      <span class="contact-text">Producer,&nbsp; Editor, Thinker</span>
    </div>

    <div class="contact-row row-phone">
      <span class="contact-icon">
        <svg width="26" height="26" viewBox="0 0 24 24" aria-hidden="true">
          <path fill="#38b6e8" d="M6.6 10.8c1.4 2.8 3.8 5.1 6.6 6.6l2.2-2.2c.3-.3.7-.4 1-.2 1.1.4 2.3.6 3.6.6.6 0 1 .4 1 1V20c0 .6-.4 1-1 1C10.6 21 3 13.4 3 4c0-.6.4-1 1-1h3.5c.6 0 1 .4 1 1 0 1.3.2 2.5.6 3.6.1.3 0 .7-.2 1l-2.3 2.2z"/>
        </svg>
      </span>
      <span class="contact-text">+61 492&nbsp;&nbsp; 157 630</span>
    </div>

    <div class="contact-row row-email">
      <span class="contact-icon">
        <svg width="26" height="26" viewBox="0 0 26 26" aria-hidden="true">
          <circle cx="13" cy="13" r="4.5" fill="none" stroke="#38b6e8" stroke-width="2.6"/>
          <path d="M17.5 9 V15 Q17.5 18 20 18 Q23.5 18 23.5 13 A10.5 10.5 0 1 0 18 22.3" fill="none" stroke="#38b6e8" stroke-width="2.6" stroke-linecap="round"/>
        </svg>
      </span>
      <span class="contact-text">pv@brightpanel.com.au</span>
    </div>

    <div class="contact-row row-web">
      <span class="contact-icon">
        <svg width="20" height="32" viewBox="0 0 20 32" aria-hidden="true">
          <path d="M4 3 L16 16 L4 29" fill="none" stroke="#38b6e8" stroke-width="3.5" stroke-linecap="round" stroke-linejoin="round"/>
        </svg>
      </span>
      <span class="contact-text">www.brightpanel.com.au</span>
    </div>
  </section>

</main>
</body>
</html>
```